New Business Card for Casual Beachfront Cafe

Quirky Beachfront Cafe at Moana, South Australia needs a DOUBLE SIDED business card to print on PrintHarbor.

Target Market(s)

Business Cards sit on the counter for Guests to take with them. Please view our website www.saltreefcafe.com.au to get a feel for the Cafe. You may also view our Instagram at @saltreefcafe

Industry/Entity Type

Cafe / Restaurant

Contact Information for Business Card

Information equivalent to: Breakfast, Lunch, Dinner, Coffee, Takeaway / 117 Parade Moana SA 5169 / Menu & Opening Hours: www.saltreefcafe.com.au / ph (08) 8461 9273

Requirements
Must have
• Information equivalent to: Breakfast, Lunch, Dinner, Coffee, Takeaway / 117 Parade Moana SA 5169 / Menu & Opening Hours: www.saltreefcafe.com.au / ph (08) 8461 9273
Nice to have
• Potentially some of our trademark colours (Cafe can be searched via Seekly)
Should not have
• Must NOT have image of the building. May have the logo provided on one side but not necessarily, depending on how you wish to design the card

```html
<!DOCTYPE html>
<html lang="en">
<head>
<meta charset="utf-8">
<title>Salt Reef Cafe – Business Card</title>
<link href="https://fonts.googleapis.com/css2?family=Lexend+Exa:wght@300;500;700&display=swap" rel="stylesheet">
<style>
  :root {
    --backdrop-top: #8a8a8a;
    --backdrop-bottom: #626262;
    --sea-blue: #164a86;
    --sea-blue-deep: #06346e;
    --sun-yellow: #f6fa0a;
    --rust: #c25a12;
    --white: #f4f6fb;
    --card-w: 540px;
    --card-h: 330px;
  }
  * { box-sizing: border-box; margin: 0; padding: 0; }
  html, body {
    width: 1200px;
    height: 915px;
    overflow: hidden;
  }
  body {
    background: linear-gradient(180deg, var(--backdrop-top), var(--backdrop-bottom));
    font-family: "Lexend Exa", sans-serif;
    display: flex;
    align-items: center;
    justify-content: center;
    gap: 40px;
  }
  .card {
    position: relative;
    width: var(--card-w);
    height: var(--card-h);
    overflow: hidden;
    box-shadow: 0 18px 40px rgba(0, 0, 0, 0.35);
  }

  /* Back side: contact details */
  .card--back {
    background: linear-gradient(160deg, var(--sea-blue), var(--sea-blue-deep));
    padding: 34px 40px;
  }
  .card--back .brand-name {
    position: absolute;
    top: 34px;
    right: 40px;
    color: var(--sun-yellow);
    font-weight: 700;
    font-size: 20px;
    letter-spacing: 0.02em;
    text-transform: uppercase;
  }
  .offer-line {
    margin-top: 96px;
    color: var(--sun-yellow);
    font-weight: 500;
    font-size: 14.5px;
    letter-spacing: 0.03em;
  }
  .contact-list {
    list-style: none;
    margin-top: 16px;
    display: grid;
    gap: 8px;
  }
  .contact-item {
    display: flex;
    align-items: center;
    gap: 10px;
    color: var(--white);
    font-weight: 300;
    font-size: 13px;
    letter-spacing: 0.04em;
  }
  .contact-item svg {
    width: 14px;
    height: 14px;
    flex: none;
    fill: none;
    stroke: var(--rust);
    stroke-width: 2;
  }
  .contact-label {
    color: var(--sun-yellow);
    font-weight: 500;
    font-size: 13px;
    letter-spacing: 0.03em;
    padding-left: 24px;
  }

  /* Front side: name */
  .card--front {
    background: linear-gradient(170deg, var(--sea-blue), var(--sea-blue-deep));
  }
  .front-band {
    position: absolute;
    inset: 0 0 auto 0;
    height: 42%;
    background: var(--sun-yellow);
  }
  .card--front .brand-name {
    position: absolute;
    left: 0;
    right: 0;
    top: 42%;
    transform: translateY(-50%);
    text-align: center;
    color: var(--sun-yellow);
    font-weight: 700;
    font-size: 40px;
    letter-spacing: 0.02em;
    text-transform: uppercase;
    padding-top: 90px;
  }
</style>
</head>
<body>

  <section class="card card--back" aria-label="Business card back">
    <p class="brand-name">Salt Reef Cafe</p>
    <p class="offer-line">Breakfast, Lunch, Dinner, Coffee, Takeaway</p>
    <ul class="contact-list">
      <li class="contact-item">
        <svg viewBox="0 0 24 24" aria-hidden="true"><path d="M12 22s7-7 7-12a7 7 0 0 0-14 0c0 5 7 12 7 12z"/><circle cx="12" cy="10" r="2.5"/></svg>
        117 Parade Moana SA 5169
      </li>
      <li class="contact-label">Menu &amp; Opening Hours:</li>
      <li class="contact-item">
        <svg viewBox="0 0 24 24" aria-hidden="true"><circle cx="12" cy="12" r="9"/><path d="M3 12h18M12 3c3 3 3 15 0 18M12 3c-3 3-3 15 0 18"/></svg>
        www.saltreefcafe.com.au
      </li>
      <li class="contact-item">
        <svg viewBox="0 0 24 24" aria-hidden="true"><path d="M6 3l3 1 1 5-2 1a11 11 0 0 0 6 6l1-2 5 1 1 3c0 2-2 3-4 3C10 21 3 14 3 7c0-2 1-4 3-4z"/></svg>
        (08) 8461 9273
      </li>
    </ul>
  </section>

  <section class="card card--front" aria-label="Business card front">
    <div class="front-band"></div>
    <p class="brand-name">Salt Reef Cafe</p>
  </section>

</body>
</html>
```